Business card for a vending machine business

I need a business card for my vending machine business. The name is Kestrel Snackworks, LLC. The card is one-sided, and landscape format. Not portrait.

The information for the card is as follows:

Dana Whitlow
Owner
(555) 314-2907
Kestrelsnackworks.example
Info@kestrelsnackworks.example

I'd like colors and design elements to match what's in my logo and company name. I'd like to have the checkered flag or racing stripe if possible You can use a border if youd like. You can use a background color if it looks nice and doesn't clash with the logo
Use your creativity. But a white background is perfectly fine. The card can be as simple, yet gets the point across to match the company name and logo.

I uploaded a copy of my logo. I also uploaded a businesses card I started to create, but since it was missing something, I gave up. Another upload has a red thunderbolt and the checkerer flag. Those two uploads are for inspiration. Again, please make sure to make the card landscape, not portrait. Thank you, designers. Good luck to all.

```html
<!DOCTYPE html>
<html lang="en">
<head>
<meta charset="utf-8">
<title>Kestrel Snackworks – Business Card</title>
<link rel="stylesheet" href="https://fonts.googleapis.com/css2?family=Montserrat:wght@400;500;700&display=swap">
<style>
  :root {
    --stage: #e9e9ea;
    --card: #ffffff;
    --brand-red: #e3262d;
    --ink: #2b2b2b;
    --muted: #555555;
    --icon-blue: #1f6fa8;
  }
  * { box-sizing: border-box; margin: 0; padding: 0; }
  html, body {
    width: 1200px;
    height: 875px;
    overflow: hidden;
    background: var(--stage);
    font-family: "Montserrat", sans-serif;
  }
  .canvas {
    width: 1200px;
    height: 875px;
    display: flex;
    align-items: center;
    justify-content: center;
  }
  .business-card {
    position: relative;
    width: 1000px;
    height: 572px;
    background: var(--card);
    border-radius: 34px;
    box-shadow: 0 10px 30px rgba(0,0,0,0.12);
  }
  .brand-mark {
    position: absolute;
    left: 150px;
    top: 236px;
    width: 360px;
    display: flex;
    align-items: center;
    gap: 14px;
  }
  .brand-dot {
    flex: none;
    width: 26px;
    height: 26px;
    border-radius: 50%;
    background: var(--brand-red);
  }
  .brand-name {
    font-weight: 700;
    font-size: 34px;
    line-height: 1.1;
    color: var(--brand-red);
  }
  .divider {
    position: absolute;
    left: 545px;
    top: 170px;
    width: 2px;
    height: 232px;
    background: var(--brand-red);
  }
  .contact-block {
    position: absolute;
    left: 578px;
    top: 176px;
  }
  .person-name {
    font-weight: 700;
    font-size: 38px;
    color: var(--brand-red);
    line-height: 1.1;
  }
  .person-title {
    font-weight: 500;
    font-size: 20px;
    color: var(--muted);
    margin-top: 4px;
    margin-bottom: 26px;
  }
  .contact-list { list-style: none; }
  .contact-item {
    display: flex;
    align-items: center;
    gap: 14px;
    font-size: 20px;
    color: var(--ink);
    margin-bottom: 16px;
  }
  .contact-icon {
    flex: none;
    width: 20px;
    height: 20px;
    fill: var(--icon-blue);
  }
</style>
</head>
<body>
<main class="canvas">
  <section class="business-card">
    <div class="brand-mark">
      <span class="brand-dot"></span>
      <span class="brand-name">Kestrel Snackworks</span>
    </div>

    <div class="divider"></div>

    <div class="contact-block">
      <h1 class="person-name">Dana Whitlow</h1>
      <p class="person-title">Owner</p>
      <ul class="contact-list">
        <li class="contact-item">
          <svg class="contact-icon" viewBox="0 0 24 24" aria-hidden="true"><path d="M6.6 10.8a15.1 15.1 0 0 0 6.6 6.6l2.2-2.2a1 1 0 0 1 1-.25 11.4 11.4 0 0 0 3.6.57 1 1 0 0 1 1 1V20a1 1 0 0 1-1 1A17 17 0 0 1 3 4a1 1 0 0 1 1-1h3.5a1 1 0 0 1 1 1c0 1.25.2 2.45.57 3.6a1 1 0 0 1-.25 1z"/></svg>
          <span>(555) 314-2907</span>
        </li>
        <li class="contact-item">
          <svg class="contact-icon" viewBox="0 0 24 24" aria-hidden="true"><path d="M2 5h20v14H2z M4 7v.5l8 5 8-5V7l-8 5z" fill-rule="evenodd"/></svg>
          <span>Info@kestrelsnackworks.example</span>
        </li>
        <li class="contact-item">
          <svg class="contact-icon" viewBox="0 0 24 24" aria-hidden="true"><path d="M12 2a10 10 0 1 0 0 20 10 10 0 0 0 0-20zm6.9 6h-3a15.6 15.6 0 0 0-1.4-3.6A8 8 0 0 1 18.9 8zM12 4c.8 1.2 1.5 2.5 1.9 4h-3.8c.4-1.5 1.1-2.8 1.9-4zM4.3 14a8 8 0 0 1 0-4h3.4a16.5 16.5 0 0 0 0 4zm.8 2h3a15.6 15.6 0 0 0 1.4 3.6A8 8 0 0 1 5.1 16zm3-8h-3a8 8 0 0 1 4.4-3.6A15.6 15.6 0 0 0 8.1 8zM12 20c-.8-1.2-1.5-2.5-1.9-4h3.8c-.4 1.5-1.1 2.8-1.9 4zm2.3-6H9.7a14.7 14.7 0 0 1 0-4h4.6a14.7 14.7 0 0 1 0 4zm.2 5.6a15.6 15.6 0 0 0 1.4-3.6h3a8 8 0 0 1-4.4 3.6zm1.8-5.6a16.5 16.5 0 0 0 0-4h3.4a8 8 0 0 1 0 4z"/></svg>
          <span>www.Kestrelsnackworks.example</span>
        </li>
      </ul>
    </div>
  </section>
</main>
</body>
</html>
```